Studying Effectively To Do List

I am looking to design a new "Study To Do List" for High School students (Ages 15 - 18) . This will be printed as an A4 notepad and so should only be a single A4 page.

The Design will need to be professional and look semi-serious but also be appealing to High school students (Ages 15 - 18) and should NOT be gender specific.

I have attached a word document outlining the structure of the page. The space provided should be large enough that people can write in it comfortably.

The notepad will most likely be printed in black and white but I'm also looking at coloured options - colours should be kept to a minimum.

This will be printed professionally and should also include a 3mm bleed.

The design should also include the business logo (included in the word document)

Target Market(s)

High School students (Ages 15 - 18). Both genders

Industry/Entity Type

Education

Font styles to use
Serif
Sans Serif

Requirements
Must have
• Please see the word document attached.
Should not have
• Too much colour

```html
<!DOCTYPE html>
<html lang="en">
<head>
<meta charset="utf-8">
<title>Northline Study Co. – Study To Do List</title>
<link rel="stylesheet" href="https://fonts.googleapis.com/css2?family=Fira+Sans:wght@400;500;600&display=swap">
<style>
  :root {
    --navy: #1f3a55;
    --orange: #e5771e;
    --paper: #ececee;
    --shade: #d6d6da;
    --rule: #8c8f96;
    --ink: #2a2d33;
    --backdrop: #c9ced5;
  }
  * { margin: 0; padding: 0; box-sizing: border-box; }
  html, body { width: 1200px; height: 1200px; overflow: hidden; }
  body {
    background: var(--backdrop);
    font-family: "Fira Sans", Arial, sans-serif;
    color: var(--ink);
    position: relative;
  }
  .sheet {
    position: absolute; left: 176px; top: 0;
    width: 848px; height: 1200px;
    background: var(--paper);
  }
  .brand-mark {
    position: absolute; left: 62px; top: 72px;
    width: 100px; height: 100px;
    border: 4px solid var(--navy); border-radius: 50%;
    display: flex; align-items: center; justify-content: center;
    font-weight: 600; font-size: 30px; color: var(--navy);
  }
  .brand-title {
    position: absolute; left: 190px; top: 80px;
    font-weight: 600; font-size: 22px; color: var(--navy);
  }
  .brand-tagline {
    position: absolute; left: 190px; top: 112px;
    font-size: 14px; line-height: 17px; font-weight: 500; color: var(--orange);
  }
  .date-field {
    position: absolute; left: 498px; top: 86px;
    font-size: 16px; color: var(--navy);
  }
  .date-line {
    position: absolute; left: 552px; top: 100px; width: 234px;
    border-bottom: 1px dotted var(--navy);
  }
  .block {
    position: absolute; left: 61px; width: 725px;
    border: 1px solid var(--rule);
  }
  .block-head {
    background: var(--navy); color: #fff; height: 31px;
    display: grid; font-weight: 600; font-size: 15px;
    align-items: end; padding-bottom: 3px;
  }
  .block-head span { text-align: center; }
  .rows { display: grid; }
  .cell {
    border-right: 1px solid var(--rule); border-top: 1px solid var(--rule);
    font-size: 11px; padding: 5px 5px; font-weight: 500;
  }
  .cell.last { border-right: none; }
  .cell.shade { background: var(--shade); }
  .cell.span2 { grid-column: span 2; }

  .revision { top: 187px; }
  .revision .block-head { grid-template-columns: 1fr; }
  .revision .rows { grid-template-columns: 371px 1fr; grid-auto-rows: 43.5px; }

  .planner { top: 317px; }
  .planner .block-head { grid-template-columns: 371px 1fr; }
  .planner .rows { grid-template-columns: 371px 177px 1fr; grid-auto-rows: 105px; }

  .notes { top: 990px; }
  .notes .block-head { grid-template-columns: 373px 1fr; }
  .notes .block-head span:last-child { text-align: left; padding-left: 5px; }
  .notes .rows { grid-template-columns: 186px 187px 1fr; grid-auto-rows: 58px; }

  .footer-band {
    position: absolute; left: 0; bottom: 0; width: 100%; height: 20px;
    display: grid; grid-template-columns: 583px 1fr;
  }
  .footer-band .navy { background: var(--navy); }
  .footer-band .orange { background: var(--orange); }
</style>
</head>
<body>
  <main class="sheet">
    <div class="brand-mark">NSC</div>
    <h1 class="brand-title">Northline Study Co.</h1>
    <p class="brand-tagline">High School English<br>Tutor ONLINE</p>
    <div class="date-field">Date</div>
    <div class="date-line"></div>

    <section class="block revision">
      <div class="block-head"><span>REVISION</span></div>
      <div class="rows">
        <div class="cell">1</div><div class="cell last">2</div>
        <div class="cell shade">3</div><div class="cell shade last">4</div>
      </div>
    </section>

    <section class="block planner">
      <div class="block-head"><span>HOMEWORK</span><span>ASSESSMENTS</span></div>
      <div class="rows">
        <div class="cell shade">Subject :</div><div class="cell shade">Assessment :</div><div class="cell shade last">Due :</div>
        <div class="cell">Task :</div><div class="cell span2 last">Element :</div>
        <div class="cell shade">Subject :</div><div class="cell shade">Assessment :</div><div class="cell shade last">Due :</div>
        <div class="cell">Task :</div><div class="cell span2 last">Element :</div>
        <div class="cell shade">Subject :</div><div class="cell shade">Assessment :</div><div class="cell shade last">Due :</div>
        <div class="cell">Task :</div><div class="cell span2 last">Element :</div>
      </div>
    </section>

    <section class="block notes">
      <div class="block-head"><span>NOTE</span><span>PRACTICE</span></div>
      <div class="rows">
        <div class="cell">1</div><div class="cell">2</div><div class="cell last"></div>
        <div class="cell shade">3</div><div class="cell shade">4</div><div class="cell shade last"></div>
      </div>
    </section>

    <div class="footer-band"><div class="navy"></div><div class="orange"></div></div>
  </main>
</body>
</html>
```